April 11th Event- Islamorada- Coaching/Tarot/Hypnotherapy

Hi! Need a flyer that can also be posted on social media. Directions attached. Also will need a version that 2 can fit on 1 piece of paper so I can cut in half for hand outs. PDF example attached as well so you can understand. Thank you!

AAAAAAAAAAAAAAAAAAAAAAAAAAAAAAAAAAAAAAAAAAAAAAAAAAAAAAAAAAAAAAAAAAAAAAAAAAAAAAAAAAAAAAAAAAAAAAAAAAAAAAAAAAAAAAAAAAAAAAAAAAAAAAAAAAAAAAAAAAAAAAAAAAAAAAAAAAAAAAAAAAAAAAAAAAAAAAAAAAAAAAAAAAAAAAAAAAAAAAAAAAAAAAAAAAAAAAAAAAAAAAAAAA

Target Market(s)

Female audience age 35-70.
Spiritual, sophisticated

Industry/Entity Type

Event Planning

Font styles to use
Serif

Colors
d2a4cc
3176b5
85acd3
b868aa
e667a6
eea4c8
f59296
fbf289
add136

Requirements
Must have
• See attachments
Nice to have
• See attachments

```html
<!DOCTYPE html>
<html lang="en">
<head>
<meta charset="utf-8">
<title>Get The 411 – Half-Page Handout Sheet</title>
<link href="https://fonts.googleapis.com/css2?family=Yellowtail&family=Catamaran:wght@400;500;600;700&display=swap" rel="stylesheet">
<style>
  :root{
    --orchid:#b868aa;
    --orchid-band:#c27db6;
    --rose:#e667a6;
    --blush:#eea4c8;
    --blush-soft:#fcebf4;
    --lilac:#d2a4cc;
    --blue:#3176b5;
    --sky:#85acd3;
    --lemon:#fbf289;
    --coral:#f59296;
    --ink:#141414;
    --paper:#ffffff;
    --backdrop:#d9d9d9;
  }
  *{box-sizing:border-box;margin:0;padding:0}
  html,body{width:1200px;height:960px;overflow:hidden;background:var(--backdrop)}
  body{font-family:"Catamaran",sans-serif;color:var(--ink)}
  .sheet{
    position:absolute;left:40px;top:83px;width:1167px;height:827px;
    transform:scale(0.96);transform-origin:0 0;
    display:flex;background:var(--paper);
  }
  .flyer{position:relative;width:583.5px;height:827px;overflow:hidden;background:var(--paper)}
  .flyer + .flyer{border-left:1px solid #333}
  .script{font-family:"Yellowtail",cursive;font-weight:400}
  .title{position:absolute;top:14px;width:100%;text-align:center;font-size:70px;color:var(--orchid);line-height:1}
  .tagline{position:absolute;top:88px;width:100%;text-align:center;font-size:29px;color:var(--rose);line-height:1}
  .invite{position:absolute;top:132px;width:100%;text-align:center;font-size:15.5px;font-weight:600}
  .swoosh{position:absolute;top:150px;left:0;width:100%;height:70px}
  .detail{
    position:absolute;top:238px;height:116px;border:1.5px solid var(--blush);border-radius:9px;
    background:var(--blush-soft);text-align:center;font-size:13.5px;line-height:20px;padding-top:12px;
  }
  .detail h3{font-family:"Yellowtail",cursive;font-weight:400;color:var(--blue);font-size:22px;line-height:26px;margin-bottom:6px}
  .detail.when{left:30px;width:92px}
  .detail.time{left:144px;width:148px}
  .detail.where{left:313px;width:240px;font-size:12.5px}
  .speakers{position:absolute;top:378px;left:0;width:100%;height:118px;background:var(--orchid-band);text-align:center;color:#fff;font-size:14px;line-height:23px}
  .speakers h2{font-family:"Yellowtail",cursive;font-weight:400;color:var(--lemon);font-size:22px;line-height:26px;margin:5px 0 4px}
  .speakers .name{color:var(--lemon)}
  .tickets{position:absolute;top:505px;left:20px;width:265px;text-align:center}
  .tickets .label{font-size:33px;font-weight:700;color:var(--orchid);line-height:40px;letter-spacing:.5px}
  .tickets .price{font-size:40px;font-weight:700;color:var(--orchid);line-height:40px}
  .tickets .price small{font-size:28px;font-weight:500}
  .tickets .drinks{font-size:21px;font-weight:500;margin-top:8px;line-height:26px}
  .tickets .note{font-size:15.5px;margin-top:8px}
  .contact{position:absolute;top:508px;left:278px;width:280px;text-align:center}
  .contact .head{font-size:17.5px;font-weight:700;color:var(--orchid);line-height:21px}
  .contact svg{display:block;margin:14px auto 2px}
  .contact .email{font-size:15px}
  .contact .phone{font-size:16.5px;font-weight:700}
  .contact .icon-phone{margin-top:6px}
  .sendoff{position:absolute;top:666px;left:203px;width:177px;height:31px;background:var(--orchid);color:#fff;font-size:20px;text-align:center;line-height:31px}
  .gallery{position:absolute;left:0;top:660px;width:100%;height:167px}
</style>
</head>
<body>
<main class="sheet">
  <article class="flyer">
    <h1 class="title script">Get The 411</h1>
    <p class="tagline script">Open Yourself Up To The Info You Have Inside</p>
    <p class="invite">Please Join Us For An Evening of Self Discovery, and Enlightment and Fun!</p>
    <svg class="swoosh" viewBox="0 0 584 70" preserveAspectRatio="none" aria-hidden="true">
      <path d="M0 6 Q292 90 584 6" fill="none" stroke="var(--lilac)" stroke-width="3"/>
      <path d="M0 24 Q292 90 584 16" fill="none" stroke="var(--orchid)" stroke-width="3"/>
    </svg>
    <section class="detail when"><h3>When:</h3>Thursday<br>11th April</section>
    <section class="detail time"><h3>Time:</h3>Doors Open at 5:30.<br>Event from 6pm-8pm.</section>
    <section class="detail where"><h3>Where:</h3>The Gardens at Palm Haven-<br>74210 Coastal Highway Islamorada<br>(MM74 Bayside behind Harbor Market)</section>
    <section class="speakers">
      <h2>Speakers:</h2>
      <p><span class="name">Rosalyn Hartwell-</span>&nbsp; The Bright Path Life Coach- Certified Professional Life Coach</p>
      <p><span class="name">Dana Whitcombe-</span>&nbsp; Licensed Hypnotherapist- Willow Moon Healing Studio</p>
      <p><span class="name">Lena Marchetti-</span>&nbsp; Tarot Readings/ True North Spiritual Counselor</p>
    </section>
    <section class="tickets">
      <p class="label">TICKETS</p>
      <p class="price">$15 <small>each</small></p>
      <p class="drinks">Drinks included.</p>
      <p class="note">Names must be on the guest list</p>
    </section>
    <section class="contact">
      <p class="head">Contact Rosalyn Hartwell<br>for tickets:</p>
      <svg width="14" height="11" viewBox="0 0 14 11" aria-hidden="true"><rect x=".6" y=".6" width="12.8" height="9.8" fill="none" stroke="var(--orchid)" stroke-width="1.1"/><path d="M.6 .6 7 6 13.4 .6" fill="none" stroke="var(--orchid)" stroke-width="1.1"/></svg>
      <p class="email">Rosalyn@brightpathlifecoach.com</p>
      <svg class="icon-phone" width="13" height="13" viewBox="0 0 13 13" aria-hidden="true"><circle cx="6.5" cy="6.5" r="5.8" fill="none" stroke="var(--orchid)" stroke-width="1.1"/><path d="M4.3 3.6 5.4 3.4 6 5 5.3 5.6Q6 7.2 7.4 7.7L8 7 9.6 7.6 9.4 8.7Q6.6 9.3 4.3 3.6Z" fill="var(--orchid)"/></svg>
      <p class="phone">305-555-0148</p>
    </section>
    <p class="sendoff script">Hope to see you there!</p>
    <svg class="gallery" viewBox="0 0 584 167" aria-hidden="false">
      <defs>
        <linearGradient id="g1-office" x1="0" y1="0" x2="1" y2="1"><stop offset="0" stop-color="#f1ece6"/><stop offset="1" stop-color="#c9a37f"/></linearGradient>
        <linearGradient id="g1-tarot" x1="0" y1="0" x2="1" y2="1"><stop offset="0" stop-color="#5b3a4e"/><stop offset="1" stop-color="#e0b23c"/></linearGradient>
        <linearGradient id="g1-relax" x1="0" y1="0" x2="1" y2="1"><stop offset="0" stop-color="#efd7c6"/><stop offset="1" stop-color="#f7f3f1"/></linearGradient>
      </defs>
      <circle cx="103" cy="160" r="108" fill="none" stroke="var(--orchid)" stroke-width="3"/>
      <circle cx="103" cy="160" r="100" fill="url(#g1-office)" stroke="var(--coral)" stroke-width="2" role="img" aria-label="Photo of a life coaching session at a desk"/>
      <circle cx="290" cy="160" r="83" fill="none" stroke="var(--orchid)" stroke-width="3"/>
      <circle cx="290" cy="160" r="76" fill="url(#g1-tarot)" stroke="var(--coral)" stroke-width="2" role="img" aria-label="Photo of tarot cards and a crystal pendulum"/>
      <circle cx="482" cy="143" r="116" fill="none" stroke="var(--orchid)" stroke-width="3"/>
      <circle cx="482" cy="143" r="108" fill="url(#g1-relax)" stroke="var(--coral)" stroke-width="2" role="img" aria-label="Photo of a woman relaxing during a crystal healing session"/>
    </svg>
  </article>

  <article class="flyer">
    <h1 class="title script">Get The 411</h1>
    <p class="tagline script">Open Yourself Up To The Info You Have Inside</p>
    <p class="invite">Please Join Us For An Evening of Self Discovery, and Enlightment and Fun!</p>
    <svg class="swoosh" viewBox="0 0 584 70" preserveAspectRatio="none" aria-hidden="true">
      <path d="M0 6 Q292 90 584 6" fill="none" stroke="var(--lilac)" stroke-width="3"/>
      <path d="M0 24 Q292 90 584 16" fill="none" stroke="var(--orchid)" stroke-width="3"/>
    </svg>
    <section class="detail when"><h3>When:</h3>Thursday<br>11th April</section>
    <section class="detail time"><h3>Time:</h3>Doors Open at 5:30.<br>Event from 6pm-8pm.</section>
    <section class="detail where"><h3>Where:</h3>The Gardens at Palm Haven-<br>74210 Coastal Highway Islamorada<br>(MM74 Bayside behind Harbor Market)</section>
    <section class="speakers">
      <h2>Speakers:</h2>
      <p><span class="name">Rosalyn Hartwell-</span>&nbsp; The Bright Path Life Coach- Certified Professional Life Coach</p>
      <p><span class="name">Dana Whitcombe-</span>&nbsp; Licensed Hypnotherapist- Willow Moon Healing Studio</p>
      <p><span class="name">Lena Marchetti-</span>&nbsp; Tarot Readings/ True North Spiritual Counselor</p>
    </section>
    <section class="tickets">
      <p class="label">TICKETS</p>
      <p class="price">$15 <small>each</small></p>
      <p class="drinks">Drinks included.</p>
      <p class="note">Names must be on the guest list</p>
    </section>
    <section class="contact">
      <p class="head">Contact Rosalyn Hartwell<br>for tickets:</p>
      <svg width="14" height="11" viewBox="0 0 14 11" aria-hidden="true"><rect x=".6" y=".6" width="12.8" height="9.8" fill="none" stroke="var(--orchid)" stroke-width="1.1"/><path d="M.6 .6 7 6 13.4 .6" fill="none" stroke="var(--orchid)" stroke-width="1.1"/></svg>
      <p class="email">Rosalyn@brightpathlifecoach.com</p>
      <svg class="icon-phone" width="13" height="13" viewBox="0 0 13 13" aria-hidden="true"><circle cx="6.5" cy="6.5" r="5.8" fill="none" stroke="var(--orchid)" stroke-width="1.1"/><path d="M4.3 3.6 5.4 3.4 6 5 5.3 5.6Q6 7.2 7.4 7.7L8 7 9.6 7.6 9.4 8.7Q6.6 9.3 4.3 3.6Z" fill="var(--orchid)"/></svg>
      <p class="phone">305-555-0148</p>
    </section>
    <p class="sendoff script">Hope to see you there!</p>
    <svg class="gallery" viewBox="0 0 584 167" aria-hidden="false">
      <defs>
        <linearGradient id="g2-office" x1="0" y1="0" x2="1" y2="1"><stop offset="0" stop-color="#f1ece6"/><stop offset="1" stop-color="#c9a37f"/></linearGradient>
        <linearGradient id="g2-tarot" x1="0" y1="0" x2="1" y2="1"><stop offset="0" stop-color="#5b3a4e"/><stop offset="1" stop-color="#e0b23c"/></linearGradient>
        <linearGradient id="g2-relax" x1="0" y1="0" x2="1" y2="1"><stop offset="0" stop-color="#efd7c6"/><stop offset="1" stop-color="#f7f3f1"/></linearGradient>
      </defs>
      <circle cx="103" cy="160" r="108" fill="none" stroke="var(--orchid)" stroke-width="3"/>
      <circle cx="103" cy="160" r="100" fill="url(#g2-office)" stroke="var(--coral)" stroke-width="2" role="img" aria-label="Photo of a life coaching session at a desk"/>
      <circle cx="290" cy="160" r="83" fill="none" stroke="var(--orchid)" stroke-width="3"/>
      <circle cx="290" cy="160" r="76" fill="url(#g2-tarot)" stroke="var(--coral)" stroke-width="2" role="img" aria-label="Photo of tarot cards and a crystal pendulum"/>
      <circle cx="482" cy="143" r="116" fill="none" stroke="var(--orchid)" stroke-width="3"/>
      <circle cx="482" cy="143" r="108" fill="url(#g2-relax)" stroke="var(--coral)" stroke-width="2" role="img" aria-label="Photo of a woman relaxing during a crystal healing session"/>
    </svg>
  </article>
</main>
</body>
</html>
```